Business Card Design

Electronic Security
Alarm Systems
CCTV
Electronic Access Control
Security System Integration

Industry/Entity Type

Business

Contact Information for Business Card

Declan Whitfield
PO Box 862
Carrowbrook Qld 4179
Phone 07 38265014
Mob 0428615937

```html
<!DOCTYPE html>
<html lang="en">
<head>
<meta charset="utf-8">
<title>Sentra – Business Card</title>
<link rel="stylesheet" href="https://fonts.googleapis.com/css2?family=Open+Sans:wght@400;600&display=swap">
<style>
  :root {
    --navy: #1a1f5c;
    --deep-blue: #1d2c93;
    --royal-blue: #3e63c9;
    --brand-red: #b5321f;
    --cyan-ring: #1cb4e6;
    --lavender: #c9c6f0;
    --card-white: #ffffff;
    --backdrop: #e9e7ec;
    --divider: #4a4a55;
  }
  * { box-sizing: border-box; margin: 0; padding: 0; }
  html, body {
    width: 1200px;
    height: 800px;
    overflow: hidden;
    background: var(--backdrop);
    font-family: "Open Sans", sans-serif;
  }
  .business-card {
    position: absolute;
    left: 75px;
    top: 100px;
    width: 1050px;
    height: 600px;
    background: var(--card-white);
    overflow: hidden;
    box-shadow: 0 10px 30px rgba(30, 30, 60, 0.18);
  }
  .card-artwork {
    position: absolute;
    inset: 0;
    width: 100%;
    height: 100%;
  }
  .holder-name {
    position: absolute;
    left: 120px;
    top: 265px;
    font-size: 30px;
    font-weight: 600;
    color: var(--navy);
  }
  .contact-divider {
    position: absolute;
    left: 378px;
    top: 388px;
    width: 2px;
    height: 92px;
    background: var(--divider);
  }
  .contact-list {
    position: absolute;
    left: 398px;
    top: 386px;
    list-style: none;
    font-size: 20px;
    color: var(--navy);
    line-height: 32px;
  }
  .contact-list li {
    display: flex;
    align-items: center;
    gap: 10px;
  }
  .contact-icon {
    width: 17px;
    height: 17px;
    flex: none;
  }
  .service-lines {
    position: absolute;
    left: 70px;
    top: 500px;
    font-size: 20px;
    color: var(--navy);
    line-height: 34px;
  }
  .service-lines .second-line { padding-left: 160px; }
  .brand-lockup {
    position: absolute;
    left: 735px;
    top: 212px;
    display: flex;
    align-items: center;
    gap: 12px;
    color: var(--navy);
  }
  .brand-mark {
    width: 30px;
    height: 30px;
    background: var(--cyan-ring);
  }
  .brand-name {
    font-size: 44px;
    font-weight: 400;
    letter-spacing: 1px;
  }
  .brand-tagline {
    border-left: 2px solid var(--divider);
    padding-left: 8px;
    font-size: 12px;
    line-height: 14px;
    width: 74px;
  }
</style>
</head>
<body>
  <main class="business-card">
    <svg class="card-artwork" viewBox="0 0 1050 600" xmlns="http://www.w3.org/2000/svg">
      <defs>
        <radialGradient id="header-glow" cx="0.15" cy="0.05" r="0.95">
          <stop offset="0" stop-color="var(--deep-blue)"/>
          <stop offset="0.35" stop-color="#4b4fc4"/>
          <stop offset="0.65" stop-color="var(--lavender)"/>
          <stop offset="0.9" stop-color="#ffffff"/>
        </radialGradient>
        <linearGradient id="photo-tone" x1="0" y1="0" x2="1" y2="1">
          <stop offset="0" stop-color="#d9dbe4"/>
          <stop offset="1" stop-color="#6c7284"/>
        </linearGradient>
      </defs>

      <path class="header-field" d="M0,0 H1050 V600 C800,180 400,160 0,140 Z" fill="url(#header-glow)"/>

      <path class="sweep-red" d="M0,140 C400,160 800,180 1050,600" fill="none" stroke="var(--brand-red)" stroke-width="12"/>
      <path class="sweep-blue" d="M0,185 C400,205 780,230 1000,640" fill="none" stroke="var(--royal-blue)" stroke-width="38"/>

      <g class="service-photos">
        <circle cx="255" cy="78" r="60" fill="url(#photo-tone)" stroke="var(--cyan-ring)" stroke-width="7" role="img" aria-label="Photo of a CCTV security camera"/>
        <circle cx="400" cy="106" r="60" fill="url(#photo-tone)" stroke="var(--cyan-ring)" stroke-width="7" role="img" aria-label="Photo of a hand pressing an alarm keypad"/>
        <circle cx="545" cy="134" r="60" fill="url(#photo-tone)" stroke="var(--cyan-ring)" stroke-width="7" role="img" aria-label="Photo of a surveillance monitoring screen"/>
      </g>
    </svg>

    <h1 class="holder-name">Declan Whitfield</h1>

    <div class="contact-divider"></div>
    <ul class="contact-list">
      <li>
        <svg class="contact-icon" viewBox="0 0 18 18"><path d="M9 1a6 6 0 0 0-6 6c0 4.5 6 10 6 10s6-5.5 6-10a6 6 0 0 0-6-6zm0 8.5A2.5 2.5 0 1 1 9 4.5a2.5 2.5 0 0 1 0 5z" fill="var(--brand-red)"/></svg>
        PO Box 862 Carrowbrook Qld 4179
      </li>
      <li>
        <svg class="contact-icon" viewBox="0 0 18 18"><path d="M4 1.5l3 3.5-1.8 1.8a10 10 0 0 0 6 6L13 11l3.5 3-1.8 2.5C8 16 2 10 1.5 3.5z" fill="var(--brand-red)"/></svg>
        Phone 07 38265014
      </li>
      <li>
        <svg class="contact-icon" viewBox="0 0 18 18"><rect x="3" y="3" width="12" height="12" rx="1.5" fill="none" stroke="var(--brand-red)" stroke-width="2"/></svg>
        Mob 0428615937
      </li>
    </ul>

    <div class="service-lines">
      <p>Electronic Security | Alarm Systems | CCTV | Electronic Access Control</p>
      <p class="second-line">Security System Integration</p>
    </div>

    <div class="brand-lockup">
      <span class="brand-mark"></span>
      <span class="brand-name">Sentra</span>
      <span class="brand-tagline">Sentra Security Systems</span>
    </div>
  </main>
</body>
</html>
```